We need a web design for a new hair care company that is based in Israel but exports its line of products around the world. We would like special features on this website that include video, sliders and other exciting effects. The final design should present information about the products and an exciting inviting image. We also will need to know how to update the site.

Designers can look at our current website and see the colors and look of the products as well. Please go to: http://lunoveltresses.com

We would like to use the colors of the Lunovel Tresses care line of products. Wordpress seems to be a good choice. We would like four pages: Home, About Us, Contact and Products.

If designers have specific questions.....please let us know!
Let the designs begin!!!!
We are waiting and excited!

Target Market(s)

Potential haircare distributors and general public

Industry/Entity Type

Hair

Requirements
Must have
• The website must have general info about what the company is, with a video, explain how to use each product and a focus on women and hair.
Nice to have
• On the website should be the logo, product info, upbeat music, video and sliders that show the exciting world of Lunovel Tresscare. It's uniqueness is that it offers Dead Sea minerals for the hair, the first of its kind.

```html
<!DOCTYPE html>
<html lang="en">
<head>
<meta charset="utf-8">
<title>Lunovel Tresscare</title>
<link rel="stylesheet" href="https://fonts.googleapis.com/css2?family=Open+Sans:wght@300;400&family=Questrial&family=Delius&family=Lora:ital@1&family=Noto+Serif&family=Arimo&display=swap">
<style>
:root{
  --brown:#5a2e0f;
  --brown-dark:#4a250b;
  --turquoise:#29bde0;
  --gold:#d9b34a;
  --gold-dark:#b48a22;
  --ink:#333;
  --muted:#666;
  --frame:#e4e4e4;
  --footer:#2b2b2b;
}
*{box-sizing:border-box;margin:0;padding:0}
html,body{width:1058px;height:1200px;overflow:hidden;background:#fff}
.page{position:relative;width:1058px;height:1200px;font-family:"Open Sans",sans-serif;color:var(--ink)}
.abs{position:absolute}

.header-pattern{left:0;top:0;width:1058px;height:63px;
  background:linear-gradient(90deg,#4fb6c6,#7d7250 25%,#48b3c4 50%,#7d7250 75%,#4fb6c6);}
.header-rule{left:0;top:63px;width:1058px;height:3px;background:var(--gold)}
.nav-bar{left:0;top:66px;width:1058px;height:72px;background:var(--brown)}
.brand{left:104px;top:78px;font-family:Questrial,sans-serif;font-size:36px;color:var(--turquoise);letter-spacing:1px;line-height:1}
.nav{left:0;top:95px;width:1058px;height:27px}
.nav a{position:absolute;top:0;height:27px;line-height:27px;font-family:Questrial,sans-serif;font-size:17px;color:#fff;text-decoration:none;transform:translateX(-50%);white-space:nowrap}
.nav a.active{background:linear-gradient(#ecca62,var(--gold-dark));color:var(--brown-dark);padding:0 11px;border-radius:2px}
.nav .sep{position:absolute;top:-4px;width:1px;height:34px;background:#6f3e1c}

.hero{left:0;top:138px;width:1058px;height:433px;
  background:
    radial-gradient(ellipse 30% 45% at 72% 55%,rgba(190,140,115,.8),transparent 70%),
    linear-gradient(90deg,#ece9e6 0%,#b58a66 18%,#6b4a34 35%,#4e3a2e 55%,#8a6652 75%,#7a5a48 100%);}
.learn-more{left:366px;top:330px;width:204px;height:53px;background:var(--turquoise);color:#fff;font-family:Questrial,sans-serif;font-size:27px;line-height:53px;padding-left:15px;text-decoration:none;white-space:nowrap}
.learn-more svg{position:absolute;right:10px;top:17px}

.intro-band{left:0;top:571px;width:1058px;height:111px;background:var(--turquoise)}
.intro-text{left:108px;top:582px;width:510px;font-size:16px;line-height:21px;color:#fff}

.video{left:632px;top:466px;width:309px;height:223px;background:#fff}
.video-screen{left:6px;top:6px;width:297px;height:211px;background:radial-gradient(ellipse at 50% 40%,#2c2c2c,#080808 75%)}
.video-title{left:0;top:56px;width:297px;text-align:center;color:#8c8c8c;font-family:Questrial,sans-serif;font-size:12px}
.video-play{left:112px;top:73px;width:73px;height:53px;background:#1e1e1e;border:1px solid #333;border-radius:3px}
.video-controls{left:8px;top:187px;width:282px;height:20px;background:#e9e9e9;border-radius:2px;font-family:Arimo,sans-serif;font-size:9px;font-weight:bold;color:#222}
.video-shadow{left:636px;top:692px;width:300px;height:10px;background:radial-gradient(ellipse at 50% 0,rgba(0,0,0,.35),transparent 70%)}

.products-title{left:101px;top:694px;font-family:Delius,cursive;font-weight:400;font-size:29px;color:var(--brown)}
.products-lead{left:104px;top:737px;font-size:11.5px;color:#222}

.card{top:786px;width:206px;height:343px;background:#fff;border:6px solid var(--frame)}
.card-image{left:0;top:0;width:194px;height:214px}
.card-label{left:0;top:181px;width:194px;height:33px;background:rgba(90,46,15,.92);color:#fff;font-family:Arimo,sans-serif;font-size:13px;line-height:33px;padding-left:11px}
.card-title{left:14px;top:232px;font-family:Lora,serif;font-style:italic;font-weight:400;font-size:17px;color:#222;white-space:nowrap}
.card-text{left:14px;top:258px;width:180px;font-family:"Noto Serif",serif;font-size:12px;line-height:18px;color:var(--muted)}
.card-link{left:14px;top:300px;font-family:"Noto Serif",serif;font-size:12px;color:#222;text-decoration:underline}

.footer{left:0;top:1152px;width:1058px;height:48px;background:var(--footer);font-family:Arimo,sans-serif;font-size:11px;color:#fff}
.footer-links{left:101px;top:17px;white-space:nowrap}
.footer-links span{margin:0 9px}
.footer-copy{right:94px;top:17px}
</style>
</head>
<body>
<div class="page">

  <header>
    <div class="abs header-pattern" role="img" aria-label="Turquoise and brown paisley pattern band"></div>
    <div class="abs header-rule"></div>
    <div class="abs nav-bar"></div>
    <div class="abs brand">Lunovel</div>
    <nav class="abs nav">
      <a class="active" href="#" style="left:501px">Home</a>
      <span class="sep" style="left:566px"></span>
      <a href="#" style="left:633px">About Us</a>
      <span class="sep" style="left:703px"></span>
      <a href="#" style="left:774px">Contact</a>
      <span class="sep" style="left:844px"></span>
      <a href="#" style="left:915px">Products</a>
    </nav>
  </header>

  <section>
    <div class="abs hero" role="img" aria-label="Hair care product bottles and jar beside a woman with long flowing brown hair"></div>
    <a class="abs learn-more" href="#">Learn More
      <svg width="24" height="20" viewBox="0 0 24 20" fill="none" stroke="#fff" stroke-width="2"><path d="M2 2l8 8-8 8M12 2l8 8-8 8"/></svg>
    </a>
    <div class="abs intro-band"></div>
    <p class="abs intro-text">Simply dummy text of the printing and typesetting industry. Lorem Ipsum has been the industry's standard dummy text ever since the 1500s, when an unknown printer took a galley of type and scram-bled it to make a type specimen book.</p>

    <div class="abs video-shadow"></div>
    <div class="abs video">
      <div class="abs video-screen">
        <div class="abs video-title">Lunovel Hair care line of products</div>
        <div class="abs video-play">
          <svg width="73" height="53" viewBox="0 0 73 53"><path d="M30 13l18 13.5L30 40z" fill="#9a9a9a"/></svg>
        </div>
        <div class="abs video-controls">
          <svg class="abs" style="left:6px;top:5px" width="8" height="10" viewBox="0 0 8 10"><path d="M0 0l8 5-8 5z" fill="#111"/></svg>
          <span class="abs" style="left:22px;top:4px">00:00</span>
          <span class="abs" style="left:60px;top:8px;width:135px;height:4px;background:#aaa"></span>
          <span class="abs" style="left:203px;top:4px">00:00</span>
          <svg class="abs" style="left:242px;top:5px" width="30" height="10" viewBox="0 0 30 10" fill="#333"><rect x="0" y="3" width="2" height="4"/><rect x="4" y="1" width="1" height="8"/><rect x="8" y="4" width="1" height="4"/><rect x="11" y="3" width="1" height="5"/><rect x="14" y="2" width="1" height="6"/><rect x="17" y="1" width="1" height="8"/><rect x="20" y="0" width="1" height="10"/><rect x="25" y="1" width="5" height="8" fill="none" stroke="#333"/></svg>
        </div>
      </div>
    </div>
  </section>

  <section>
    <h2 class="abs products-title">Lunovel Products</h2>
    <p class="abs products-lead">Shampoo and Conditioners are SLS/SLES-free and colour-safe, to deliver outstanding results on all hair types leaving you with soft, smooth, shiny hair.</p>

    <article class="abs card" style="left:94px">
      <div class="abs card-image" role="img" aria-label="Woman with long brown hair beside a product box" style="background:linear-gradient(160deg,#5e5a62,#3e2e28 55%,#8a623e)"></div>
      <div class="abs card-label">Lunovel Product 1</div>
      <h3 class="abs card-title">Donec tempor libero</h3>
      <p class="abs card-text">Lorem ipsum dolor sit amet, consectetur adipiscing elit....</p>
      <a class="abs card-link" href="#">details</a>
    </article>

    <article class="abs card" style="left:316px">
      <div class="abs card-image" role="img" aria-label="Blonde woman receiving a hair serum treatment beside a product jar" style="background:linear-gradient(160deg,#b9a48c,#e6d6c2 50%,#eee8e2)"></div>
      <div class="abs card-label">Lunovel Product 2</div>
      <h3 class="abs card-title">Vivamus vel sem at</h3>
      <p class="abs card-text">Lorem ipsum dolor sit amet, consectetur adipiscing elit....</p>
      <a class="abs card-link" href="#">details</a>
    </article>

    <article class="abs card" style="left:537px">
      <div class="abs card-image" role="img" aria-label="Woman with straight dark hair beside a product bottle" style="background:linear-gradient(160deg,#6a7884,#2c3038 50%,#5e6874)"></div>
      <div class="abs card-label">Lunovel Product 3</div>
      <h3 class="abs card-title">Etiam commodo</h3>
      <p class="abs card-text">Lorem ipsum dolor sit amet, consectetur adipiscing elit....</p>
      <a class="abs card-link" href="#">details</a>
    </article>

    <article class="abs card" style="left:760px">
      <div class="abs card-image" role="img" aria-label="Woman with curly hair receiving a scalp massage beside a product bottle" style="background:linear-gradient(160deg,#3a2418,#6e4a34 50%,#b8a394)"></div>
      <div class="abs card-label">Lunovel Product 4</div>
      <h3 class="abs card-title">Mauris posuere</h3>
      <p class="abs card-text">Lorem ipsum dolor sit amet, consectetur adipiscing elit....</p>
      <a class="abs card-link" href="#">details</a>
    </article>
  </section>

  <footer class="abs footer">
    <div class="abs footer-links">Terms of Use<span>|</span>Privacy Policy<span>|</span>Site Map<span>|</span>Contact Us<span>|</span>Select Country</div>
    <div class="abs footer-copy">© Lunovel Tresscare - All Rights Reserved</div>
  </footer>

</div>
</body>
</html>
```